IT company needs new and creative business card!

As it is very urgent, the designer who send designs first will have more chance to win.
Please send a new creative business card design with our new logo.
Please send us an 'able to edit' 'open art' as we have many employees to issue business cards (different names, positions, contacts).
The business card must show the Name of the person, position, contact the details and company information as it below:
e.g name of the person: Renato Colussi
e.g. positions Exective Director
our website www.brindlecore.com.au
e.g person's e-mail rcolussi@brindlecore.com.au
e.g. person mobile number m.+61 0400 718 354
company's address: Level 5, 14 Quarry Rd North Sydney NSW 2060

Project Deadline Extended Reason: I've just decided to update my logo (after started this project) so I am running other project to later come back here and update the brief attaching the new logo to then design the business card. Added Tuesday, February 28, 2017

Target Market(s)

IT

Industry/Entity Type

It Company

Contact Information for Business Card

The business card should show the Name of the person, position, contact the details and company information.

Requirements
Must have
• The business card must show the Name of the person, position, contact the details and company information as it below:
• e.g name of the person: Renato Colussi
• e.g. positions Exective Director
• our website www.brindlecore.com.au
• e.g person's e-mail rcolussi@brindlecore.com.au
• e.g. person mobile number m.+61 0400 718 354
• company's address: Level 5, 14 Quarry Rd North Sydney NSW 2060

```html
<!DOCTYPE html>
<html lang="en">
<head>
<meta charset="utf-8">
<title>Brindlecore business cards</title>
<link href="https://fonts.googleapis.com/css2?family=Lato:wght@400;700&display=swap" rel="stylesheet">
<style>
:root{
  --navy:#0d5aa7;
  --sky:#2fa3d8;
  --ink:#0d4d94;
  --paper:#ffffff;
  --stage:#000000;
  --rule:#b9cfe6;
  --badge:#c9ccd1;
}
*{margin:0;padding:0;box-sizing:border-box}
html,body{width:1189px;height:1200px;overflow:hidden;background:var(--stage);font-family:'Lato',sans-serif}
.canvas{position:relative;width:1189px;height:1200px}
.card-back{position:absolute;left:336px;top:110px;width:473px;height:270px;background:var(--navy);border-radius:14px;display:flex;align-items:center;justify-content:center}
.brand{display:flex;align-items:center;gap:10px;font-weight:700;letter-spacing:.5px}
.brand-dot{border-radius:50%;flex:none}
.card-back .brand{color:var(--paper);font-size:34px}
.card-back .brand-dot{width:34px;height:34px;background:var(--paper)}
.card{position:absolute;width:480px;height:274px;background:var(--paper);border-radius:14px;overflow:hidden;color:var(--ink)}
.card .brand{position:absolute;left:29px;top:112px;color:var(--navy);font-size:24px}
.card .brand-dot{width:22px;height:22px;background:var(--sky)}
.divider{position:absolute;left:243px;top:69px;width:1px;height:120px;background:var(--rule)}
.details{position:absolute;left:265px;top:64px}
.name{font-weight:700;font-size:17px;line-height:19px;color:var(--navy)}
.role{font-size:12.5px;line-height:14px;color:var(--sky)}
.cert{font-size:11px;line-height:14px;margin-top:3px}
.contacts{position:absolute;left:265px;top:137px;list-style:none;font-size:13.5px;line-height:17px}
.contacts li{display:flex;align-items:center;gap:8px}
.contacts svg{width:11px;height:11px;flex:none}
.address{position:absolute;left:26px;top:216px;font-size:13px;line-height:16px}
.badges{position:absolute;top:216px;right:74px;display:flex;gap:12px}
.badge{width:34px;height:34px;border-radius:50%;border:2px solid var(--badge);background:#f1f2f4}
.band{position:absolute;left:0;right:0;bottom:0;height:13px;display:flex}
.band span:first-child{flex:1;background:var(--navy)}
.band span:last-child{flex:1;background:var(--sky)}
</style>
</head>
<body>
<svg width="0" height="0" style="position:absolute">
  <symbol id="i-phone" viewBox="0 0 12 12"><rect x="3" y="0.5" width="6" height="11" rx="1" fill="none" stroke="#2fa3d8" stroke-width="1.2"/><rect x="4.3" y="2" width="3.4" height="6" fill="#2fa3d8"/></symbol>
  <symbol id="i-mail" viewBox="0 0 12 12"><rect x="0.5" y="2" width="11" height="8" fill="#2fa3d8"/><path d="M0.5 2l5.5 4.5 5.5-4.5" fill="none" stroke="#fff" stroke-width="1"/></symbol>
  <symbol id="i-web" viewBox="0 0 12 12"><g fill="none" stroke="#2fa3d8" stroke-width="1"><circle cx="6" cy="6" r="5.2"/><ellipse cx="6" cy="6" rx="2.3" ry="5.2"/><path d="M1 6h10M2 3.3h8M2 8.7h8"/></g></symbol>
</svg>
<div class="canvas">
  <div class="card-back"><div class="brand"><span class="brand-dot"></span>BRINDLECORE</div></div>

  <div class="card" style="left:68px;top:443px">
    <div class="brand"><span class="brand-dot"></span>BRINDLECORE</div>
    <div class="divider"></div>
    <div class="details"><p class="name">Renato Colussi</p><p class="role">Director</p><p class="cert">NDX 2016041<br>NEX 9173</p></div>
    <ul class="contacts">
      <li><svg><use href="#i-phone"/></svg>m.+61 0400 718 354</li>
      <li><svg><use href="#i-mail"/></svg>rcolussi@brindlecore.com.au</li>
      <li><svg><use href="#i-web"/></svg>www.brindlecore.com.au</li>
    </ul>
    <p class="address">Level 5, 14 Quarry Rd<br>Westmere Bay NSW 2189</p>
    <div class="badges"><span class="badge"></span><span class="badge"></span></div>
    <div class="band"><span></span><span></span></div>
  </div>

  <div class="card" style="left:644px;top:446px">
    <div class="brand"><span class="brand-dot"></span>BRINDLECORE</div>
    <div class="divider"></div>
    <div class="details"><p class="name">Tariq Hassan</p><p class="role">Network Consultant Engineer</p><p class="cert">NDX 20160093<br>NEX 23418</p></div>
    <ul class="contacts">
      <li><svg><use href="#i-phone"/></svg>+61 450 291 846</li>
      <li><svg><use href="#i-mail"/></svg>thassan@brindlecore.com.au</li>
      <li><svg><use href="#i-web"/></svg>www.brindlecore.com.au</li>
    </ul>
    <p class="address">Level 5, 14 Quarry Rd<br>Westmere Bay NSW 2189</p>
    <div class="badges"><span class="badge"></span><span class="badge"></span></div>
    <div class="band"><span></span><span></span></div>
  </div>

  <div class="card" style="left:66px;top:739px">
    <div class="brand"><span class="brand-dot"></span>BRINDLECORE</div>
    <div class="divider"></div>
    <div class="details"><p class="name">Marco Bellini</p><p class="role">Director</p><p class="cert">NEX 7352</p></div>
    <ul class="contacts">
      <li><svg><use href="#i-phone"/></svg>+61 430 562 907</li>
      <li><svg><use href="#i-mail"/></svg>mbellini@brindlecore.com.au</li>
      <li><svg><use href="#i-web"/></svg>www.brindlecore.com.au</li>
    </ul>
    <p class="address">Level 5, 14 Quarry Rd<br>Westmere Bay NSW 2189</p>
    <div class="badges"><span class="badge"></span></div>
    <div class="band"><span></span><span></span></div>
  </div>

  <div class="card" style="left:641px;top:739px">
    <div class="brand"><span class="brand-dot"></span>BRINDLECORE</div>
    <div class="divider"></div>
    <div class="details"><p class="name">Imran Qureshi</p><p class="role">Network Consultant Engineer</p><p class="cert">NEX 5918</p></div>
    <ul class="contacts">
      <li><svg><use href="#i-phone"/></svg>+61 404 317 285</li>
      <li><svg><use href="#i-mail"/></svg>iqureshi@brindlecore.com.au</li>
      <li><svg><use href="#i-web"/></svg>www.brindlecore.com.au</li>
    </ul>
    <p class="address">Level 5, 14 Quarry Rd<br>Westmere Bay NSW 2189</p>
    <div class="badges"><span class="badge"></span></div>
    <div class="band"><span></span><span></span></div>
  </div>
</div>
</body>
</html>
```